Logo needed for business card

Velistra Pty Ltd is in the business of healthcare and ecommerce.

We own and manage pharmacies and online health ecomerce sites.

We provide ecommerce consultants for companies looking for an ecommerce business startegy.

Think of it as the umbrella under which several healthcare brands may sit.

When I think of Velistra, I visulaise slick black/metalic colours, so please stay away from the common blue and green colours that seem to be so popular in this field.

Target Market(s)

CEOs and COOs

Industry/Entity Type

Healthcare

Contact Information for Business Card

Delphine Okoro
Director
Velistra Pty Ltd
4/237 Kelburn Pde
Maroubra, NSW 2035

Requirements
Must have
• Design must have scope to be implemented on the company's website and letterheads etc.

```html
<!DOCTYPE html>
<html lang="en">
<head>
<meta charset="utf-8">
<title>Velistra Business Cards</title>
<link href="https://fonts.googleapis.com/css2?family=Questrial&display=swap" rel="stylesheet">
<style>
:root{
  --stage:#2b2b2b;
  --card:#050505;
  --metal:#a9a9a9;
  --metal-light:#cfcfcf;
  --text:#9a9a9a;
  --text-soft:#8a8a8a;
  --rule:#555555;
}
*{margin:0;padding:0;box-sizing:border-box}
html,body{width:1200px;height:900px;overflow:hidden;background:var(--stage)}
body{position:relative;font-family:"Questrial",sans-serif}
.card{position:absolute;left:298px;width:630px;height:388px;background:var(--card);border-radius:22px;color:var(--text)}
.card--front{top:52px}
.card--back{top:466px;height:390px}
.brand{position:absolute;left:110px;display:flex;align-items:center;gap:22px}
.brand__dot{width:56px;height:56px;border-radius:50%;background:var(--metal)}
.brand__name{font-size:50px;color:var(--metal-light);line-height:1;letter-spacing:0.5px}
.tagline{position:absolute;left:280px;font-size:11.5px;color:var(--metal-light);font-weight:700;letter-spacing:0.2px;white-space:nowrap}
.card--front .brand{top:66px}
.card--front .tagline{top:133px}
.card--back .brand{top:66px}
.card--back .tagline{top:134px}
.company{position:absolute;left:0;width:100%;text-align:center;font-size:11px;line-height:15px;color:var(--text);font-weight:700}
.card--front .company{top:184px}
.card--back .company{top:334px;left:7px}
.person{position:absolute;left:64px;width:140px;text-align:center}
.person__name{font-size:16px;color:var(--text)}
.person__role{font-size:11px;color:var(--text-soft)}
.card--front .person{top:286px}
.card--back .person{top:252px}
.divider{position:absolute;left:360px;width:1px;height:57px;background:var(--rule)}
.card--front .divider{top:276px}
.card--back .divider{top:243px}
.contact{position:absolute;left:370px;font-size:11.5px;color:var(--text-soft);list-style:none}
.contact li{display:flex;align-items:center;height:24px}
.contact svg{width:10px;height:10px;margin-right:13px;fill:none;stroke:var(--text-soft);stroke-width:1.3}
.card--front .contact{top:280px}
.card--back .contact{top:246px}
</style>
</head>
<body>
  <section class="card card--front">
    <div class="brand"><span class="brand__dot"></span><span class="brand__name">Velistra</span></div>
    <p class="tagline">Ecommerce - Health - Strategy - Consulting</p>
    <p class="company">Velistra Pty Ltd<br>4/237 Kelburn Pde Maroubra, NSW 2035</p>
    <div class="person"><p class="person__name">Delphine Okoro</p><p class="person__role">Director</p></div>
    <span class="divider"></span>
    <ul class="contact">
      <li><svg viewBox="0 0 10 10"><path d="M2 1l2 2-1 1.5c.6 1.2 1.3 1.9 2.5 2.5L7 6l2 2-1.5 1.5C4 9 1 6 .5 2.5z"/></svg>0400 555 019</li>
      <li><svg viewBox="0 0 10 10"><circle cx="5" cy="5" r="2"/><path d="M7 5v1a1.5 1.5 0 0 0 3 0V5a5 5 0 1 0-2 4"/></svg>delphine@velistrahealth.com.au</li>
    </ul>
  </section>

  <section class="card card--back">
    <div class="brand"><span class="brand__dot"></span><span class="brand__name">Velistra</span></div>
    <p class="tagline">Ecommerce - Health - Strategy - Consulting</p>
    <div class="person"><p class="person__name">Delphine Okoro</p><p class="person__role">Director</p></div>
    <span class="divider"></span>
    <ul class="contact">
      <li><svg viewBox="0 0 10 10"><path d="M2 1l2 2-1 1.5c.6 1.2 1.3 1.9 2.5 2.5L7 6l2 2-1.5 1.5C4 9 1 6 .5 2.5z"/></svg>0400 555 019</li>
      <li><svg viewBox="0 0 10 10"><circle cx="5" cy="5" r="2"/><path d="M7 5v1a1.5 1.5 0 0 0 3 0V5a5 5 0 1 0-2 4"/></svg>delphine@velistrahealth.com.au</li>
    </ul>
    <p class="company">Velistra Pty Ltd<br>4/237 Kelburn Pde Maroubra, NSW 2035</p>
  </section>
</body>
</html>
```